Corporate Design für Austausch & Neuerrichtung von Heizungs- und Klimatechnik
Zielgruppe
Austausch, Neuerrichtung modernster Heizungstechnik und Klimatechnik
Unsere Zielgruppe sind Privatpersonen die Ihr Haus zukunftsorientiert beheizen bzw. kühlen wollen
Aufgabenstellung
schlicht, modern, klar
gerne schwarzer Hintergrund und max 3 Farben gerne auch kräftig / auffällig
Nur eine Idee: Vielleicht können kleine Icons im Logo erscheinen.... z.b. 4 Elemente.... Feuer, Wasser, Luft, Erde plus schneeflocke für die klimatechnik (?)

```html
<!DOCTYPE html>
<html lang="de">
<head>
<meta charset="utf-8">
<title>Velmora – Briefumschläge</title>
<link href="https://fonts.googleapis.com/css2?family=Arimo:wght@400&family=Source+Sans+3:wght@400&display=swap" rel="stylesheet">
<style>
  :root{
    --stage:#4b4b4b;
    --envelope:#363636;
    --seam:#4a4a4a;
    --muted:#a9a9a9;
    --window:#ffffff;
    --window-text:#555555;
    --mark:#8a8a8a;
    --brand-blue:#1a8fd8;
    --brand-navy:#2a4aa6;
    --band-start:#6cc8d8;
    --band-mid:#2a4a9a;
    --band-end:#2a2a5a;
    --brand-red:#b81c25;
  }
  *{margin:0;padding:0;box-sizing:border-box}
  html,body{width:1200px;height:1200px;overflow:hidden;background:var(--stage)}
  .envelope{position:absolute;left:270px;width:671px;height:420px}
  .envelope--plain{top:135px}
  .envelope--banded{top:669px}
  .envelope__shape{position:absolute;inset:0}
  .flap-mark{position:absolute;left:318px;top:17px;width:44px;height:44px;border-radius:50%;
    background:var(--brand-blue)}
  .sender{position:absolute;display:flex;gap:8px;align-items:flex-start;
    font:400 9.5px/13px "Source Sans 3",sans-serif;color:var(--muted)}
  .sender svg{width:11px;height:16px;flex:none;margin-top:-1px}
  .stamp{position:absolute;left:495px;top:104px;width:124px;height:73px;
    background:#fff;padding:5px;border:1px dashed #ddd}
  .stamp__picture{width:100%;height:100%;
    background:linear-gradient(160deg,#c9d4e4 0%,#a8b8c8 35%,#6f8a3a 60%,#c8b040 75%,#2c3a2a 100%)}
  .window{position:absolute;left:46px;top:262px;width:268px;height:107px;
    background:var(--window);border-radius:12px}
  .window__corner{position:absolute;width:11px;height:11px;border:0 solid var(--mark)}
  .window__corner--tl{left:26px;top:9px;border-left-width:1px;border-top-width:1px}
  .window__corner--tr{right:26px;top:9px;border-right-width:1px;border-top-width:1px}
  .window__corner--bl{left:26px;bottom:14px;border-left-width:1px;border-bottom-width:1px}
  .window__corner--br{right:26px;bottom:14px;border-right-width:1px;border-bottom-width:1px}
  .recipient{position:absolute;left:65px;top:22px;
    font:400 9.5px/14.5px "Arimo",sans-serif;color:var(--window-text)}
  .brand{position:absolute;display:flex;align-items:center;gap:10px}
  .brand__dot{width:62px;height:62px;border-radius:50%;background:var(--brand-blue);flex:none}
  .brand__name{font:400 19px/1 "Arimo",sans-serif;color:var(--brand-navy)}
  .brand__tagline{font:400 8.5px/8.5px "Arimo",sans-serif;color:var(--mark);margin-top:3px}
  .band{position:absolute;top:384px;height:7px}
  .band--gradient{left:0;width:564px;
    background:linear-gradient(90deg,var(--band-start),var(--band-mid) 55%,var(--band-end))}
  .band--red{left:620px;width:51px;background:var(--brand-red)}
  .band-dot{position:absolute;left:569px;top:364px;width:46px;height:46px;border-radius:50%;
    background:var(--brand-blue)}
</style>
</head>
<body>

<section class="envelope envelope--plain">
  <svg class="envelope__shape" viewBox="0 0 671 420" aria-hidden="true">
    <path d="M0 75 L36 9 Q41 0 52 0 L606 0 Q620 0 630 10 L671 75 Z" fill="var(--envelope)"/>
    <rect x="0" y="75" width="671" height="3" fill="var(--seam)"/>
    <rect x="0" y="78" width="671" height="342" fill="var(--envelope)"/>
  </svg>
  <span class="flap-mark"></span>
  <div class="sender" style="left:52px;top:107px">
    <svg viewBox="0 0 11 16"><path d="M5.5 0A5.5 5.5 0 0 0 0 5.5C0 9 5.5 16 5.5 16S11 9 11 5.5A5.5 5.5 0 0 0 5.5 0Zm0 7.5a2 2 0 1 1 0-4 2 2 0 0 1 0 4Z" fill="var(--mark)"/></svg>
    <p>Lindenhofer Str. 42<br>34117 Talheim am Main</p>
  </div>
  <div class="stamp"><div class="stamp__picture" role="img" aria-label="Briefmarke mit Porträtmotiv"></div></div>
  <div class="window">
    <span class="window__corner window__corner--tl"></span><span class="window__corner window__corner--tr"></span>
    <span class="window__corner window__corner--bl"></span><span class="window__corner window__corner--br"></span>
    <p class="recipient">Marlene Vossberg<br>Am Birkenweg 12<br>53111 Bergfeld<br>SCHWEIZ</p>
  </div>
  <div class="brand" style="left:450px;top:292px">
    <span class="brand__dot"></span>
    <div><p class="brand__name">Velmora</p><p class="brand__tagline">effizient<br>nachhaltig<br>persönlich</p></div>
  </div>
</section>

<section class="envelope envelope--banded">
  <svg class="envelope__shape" viewBox="0 0 671 420" aria-hidden="true">
    <path d="M0 75 L36 9 Q41 0 52 0 L606 0 Q620 0 630 10 L671 75 Z" fill="var(--envelope)"/>
    <rect x="0" y="75" width="671" height="3" fill="var(--seam)"/>
    <rect x="0" y="78" width="671" height="342" fill="var(--envelope)"/>
  </svg>
  <span class="flap-mark"></span>
  <div class="brand" style="left:46px;top:94px">
    <span class="brand__dot"></span>
    <div><p class="brand__name">Velmora</p><p class="brand__tagline">effizient<br>nachhaltig<br>persönlich</p></div>
  </div>
  <div class="sender" style="left:68px;top:188px">
    <svg viewBox="0 0 11 16"><path d="M5.5 0A5.5 5.5 0 0 0 0 5.5C0 9 5.5 16 5.5 16S11 9 11 5.5A5.5 5.5 0 0 0 5.5 0Zm0 7.5a2 2 0 1 1 0-4 2 2 0 0 1 0 4Z" fill="var(--mark)"/></svg>
    <p>Lindenhofer Str. 42<br>34117 Talheim am Main</p>
  </div>
  <div class="stamp"><div class="stamp__picture" role="img" aria-label="Briefmarke mit Porträtmotiv"></div></div>
  <div class="window" style="top:261px">
    <span class="window__corner window__corner--tl"></span><span class="window__corner window__corner--tr"></span>
    <span class="window__corner window__corner--bl"></span><span class="window__corner window__corner--br"></span>
    <p class="recipient">Marlene Vossberg<br>Am Birkenweg 12<br>53111 Bergfeld<br>SCHWEIZ</p>
  </div>
  <div class="band band--gradient"></div>
  <span class="band-dot"></span>
  <div class="band band--red"></div>
</section>

</body>
</html>
```